Very visible CoWorking Building Sign overlooking downtown LA and 110 freeway

Our building is drab but very visible and in the best location. We need a great sign for our monolith that overlooks downtown LA and the 100 freeway. We are a new CoWorking business and would like to have a few things we do on the sign: private offices, virtual offices, CoWorking Lounge. Everything we have seen is ho-hum. Can you get us noticed? We need people to know what we do and that we are here but in a creative, professional, unique sign.
Target Market(s)
People who have a business in DTLA, remote workers and those who work from home who need a professional address.
Requirements
Must have
- Our logo (which can be somewhat reimagined) which has our address 2770 on it. The three things we focus on: Private Offices, Virtual Offices, CoWorking Lounge. Incorporate some Navy. Readable from several hundred feet away.
Nice to have
- Mural feel? Something inspirational in this crazy COVID times? Graphics? Color block. I like the idea of decorative but it has to be readable as a building sign. The same with the use of colors. Our colors are grays and navy but with a pop of the chartreuse (we have 2 velvet chartreuse chairs in the space). Helpful to view our website: Brackmere2770.com.
Should not have
- Not too graffiti. Keep it professional but unique and wow.

```html
<!DOCTYPE html>
<html lang="en">
<head>
<meta charset="utf-8">
<title>Brackmere 2770 – Building Sign Options</title>
<link rel="stylesheet" href="https://fonts.googleapis.com/css2?family=Bebas+Neue&family=Crimson+Pro:ital,wght@1,500&display=swap">
<style>
  :root {
    --navy: #1e365d;
    --chartreuse: #9bca3b;
    --sky: #85aad2;
    --white: #ffffff;
    --page: #ffffff;
  }
  html, body {
    margin: 0;
    padding: 0;
    width: 1200px;
    height: 1200px;
    overflow: hidden;
    background: var(--page);
  }
  .sign {
    position: absolute;
    left: 150px;
    width: 900px;
    height: 444px;
    display: block;
  }
  .sign--chartreuse { top: 124px; --accent: var(--chartreuse); }
  .sign--sky { top: 600px; --accent: var(--sky); }
  .sign__accent-field { fill: var(--accent); }
  .sign__navy-field { fill: var(--navy); }
  .sign__divider { fill: var(--white); }
  .sign__bullet { fill: var(--accent); }
  .sign__service {
    font-family: "Bebas Neue", "Arial Narrow", sans-serif;
    font-size: 84px;
    fill: var(--white);
  }
  .sign__tagline {
    font-family: "Crimson Pro", Georgia, serif;
    font-style: italic;
    font-weight: 500;
    font-size: 80px;
    fill: var(--white);
  }
  .sign__name {
    font-family: "Bebas Neue", "Arial Narrow", sans-serif;
    font-size: 44px;
    letter-spacing: 2px;
    fill: var(--white);
  }
</style>
</head>
<body>

<svg class="sign sign--chartreuse" viewBox="0 0 1124 555" role="img" aria-label="Brackmere 2770 sign: Private Offices, Virtual Offices, Coworking Lounge. Work. Elevated.">
  <rect class="sign__accent-field" x="0" y="0" width="1124" height="555"/>
  <polygon class="sign__navy-field" points="487,0 1124,0 1124,555 337,555"/>
  <polygon class="sign__divider" points="464,0 487,0 392,352 369,352"/>
  <rect class="sign__bullet" x="525" y="94" width="23" height="23"/>
  <rect class="sign__bullet" x="525" y="182" width="23" height="23"/>
  <rect class="sign__bullet" x="525" y="271" width="23" height="23"/>
  <text class="sign__service" x="580" y="136" textLength="400" lengthAdjust="spacingAndGlyphs">PRIVATE OFFICES</text>
  <text class="sign__service" x="580" y="222" textLength="404" lengthAdjust="spacingAndGlyphs">VIRTUAL OFFICES</text>
  <text class="sign__service" x="580" y="308" textLength="479" lengthAdjust="spacingAndGlyphs">COWORKING LOUNGE</text>
  <text class="sign__tagline" x="130" y="482">Work.</text>
  <text class="sign__tagline" x="380" y="482">Elevated.</text>
  <text class="sign__name" x="880" y="484">BRACKMERE</text>
</svg>

<svg class="sign sign--sky" viewBox="0 0 1124 555" role="img" aria-label="Brackmere 2770 sign: Private Offices, Virtual Offices, Coworking Lounge. Work. Elevated.">
  <rect class="sign__accent-field" x="0" y="0" width="1124" height="555"/>
  <polygon class="sign__navy-field" points="487,0 1124,0 1124,555 337,555"/>
  <polygon class="sign__divider" points="464,0 487,0 392,352 369,352"/>
  <rect class="sign__bullet" x="525" y="94" width="23" height="23"/>
  <rect class="sign__bullet" x="525" y="182" width="23" height="23"/>
  <rect class="sign__bullet" x="525" y="271" width="23" height="23"/>
  <text class="sign__service" x="580" y="136" textLength="400" lengthAdjust="spacingAndGlyphs">PRIVATE OFFICES</text>
  <text class="sign__service" x="580" y="222" textLength="404" lengthAdjust="spacingAndGlyphs">VIRTUAL OFFICES</text>
  <text class="sign__service" x="580" y="308" textLength="479" lengthAdjust="spacingAndGlyphs">COWORKING LOUNGE</text>
  <text class="sign__tagline" x="130" y="482">Work.</text>
  <text class="sign__tagline" x="380" y="482">Elevated.</text>
  <text class="sign__name" x="880" y="484">BRACKMERE</text>
</svg>

</body>
</html>
```